Book cover design for a debut author; 'Quiet Ledgers' by Brent Hollis.

My father has written a book and I would love to gift him a bespoke front cover for it for his 60th birthday this year.
The book is a work of fiction and tells the story of two strangers (an Asian Female and a Caucasian Male) who meet on a train. After the train crashes and bursts into flames, they take the luggage of different passengers and decide to make a new life together, culminating in a murder which they believe they can get away with forever. The book is a thriller and engages the reader in suspense, excitement, anticipation and anxiety.

Target Market(s)

Thriller Fiction Readers

Font styles to use
Serif

Colors

Designer to choose colors to be used in the design.

Requirements
Must have
• A vibrant front cover with consideration over the font of both the title and author.
• I would like the train where they meet to be the main focus for the front cover. The strangers meet on a train and I’d like the cover to reflect this.
• Design must include front cover, spine and back cover with a space for blurb (to follow).
Nice to have
• A photograph based cover would I think suit the book better than an illustration.

```html
<!DOCTYPE html>
<html lang="en">
<head>
<meta charset="UTF-8">
<title>Quiet Ledgers — Book Cover Spread</title>
<link href="https://fonts.googleapis.com/css2?family=Anton&family=Courier+Prime:wght@700&family=Open+Sans:wght@400;600&display=swap" rel="stylesheet">
<style>
  :root {
    --stage: #e6e6e6;
    --ink-dark: #141414;
    --ink-mid: #2a2a2a;
    --accent-red: #c7281f;
    --spine-red: #9e2f24;
    --band-red: #d0332a;
    --paper-white: #ffffff;
    --train-blue: #3f5566;
    --train-steel: #7d8c98;
    --train-shadow: #1d2832;
    --flame-deep: #b8320c;
    --flame-bright: #ff9a1f;
    --flame-glow: #ffd25a;
  }
  * { margin: 0; padding: 0; box-sizing: border-box; }
  html, body {
    width: 1200px; height: 1000px; overflow: hidden;
    background: radial-gradient(ellipse at 50% 40%, #f4f4f4 0%, var(--stage) 70%);
    font-family: "Open Sans", sans-serif;
  }
  .spread {
    position: absolute; left: 130px; top: 180px;
    width: 940px; height: 640px;
    display: flex;
    box-shadow: 0 30px 50px rgba(0,0,0,0.25);
  }

  /* Back cover */
  .back-cover {
    position: relative; width: 440px; height: 100%;
    background: linear-gradient(180deg, var(--ink-dark) 0%, var(--ink-mid) 55%, #1c1410 100%);
    overflow: hidden;
  }
  .back-cover__heading {
    position: absolute; top: 66px; left: 0; right: 0;
    text-align: center;
    font-family: "Courier Prime", monospace; font-weight: 700;
    font-size: 21px; line-height: 1.3; letter-spacing: 3px;
    color: var(--accent-red); text-transform: uppercase;
  }
  .back-cover__blurb {
    position: absolute; top: 200px; left: 46px; right: 40px;
    color: var(--paper-white); font-size: 16px; line-height: 1.65;
    letter-spacing: 0.6px;
  }
  .back-cover__blurb p + p { margin-top: 20px; }
  .back-cover__flames {
    position: absolute; left: 0; right: 0; bottom: 0; height: 250px;
    background: linear-gradient(0deg, var(--flame-deep) 0%, var(--flame-bright) 35%, rgba(255,154,31,0.45) 65%, rgba(0,0,0,0) 100%);
  }

  /* Spine */
  .spine {
    position: relative; width: 60px; height: 100%;
    background: var(--spine-red);
    display: flex; flex-direction: column; align-items: center;
    justify-content: space-between; padding: 40px 0;
  }
  .spine__text {
    writing-mode: vertical-rl;
    color: var(--paper-white); font-size: 26px; letter-spacing: 4px;
    text-transform: uppercase; font-weight: 400;
  }
  .spine__rule { width: 2px; flex: 0 0 28px; background: var(--paper-white); margin: 14px 0; }
  .spine__author { font-weight: 600; font-size: 24px; }

  /* Front cover */
  .front-cover {
    position: relative; width: 440px; height: 100%;
    background: linear-gradient(180deg, #3a3a3a 0%, var(--ink-dark) 30%, var(--ink-dark) 100%);
    overflow: hidden;
  }
  .front-cover__smoke {
    position: absolute; inset: 0 0 auto 0; height: 240px;
    background: radial-gradient(ellipse at 35% 30%, rgba(170,170,170,0.5) 0%, rgba(0,0,0,0) 70%);
  }
  .front-cover__train {
    position: absolute; left: 14px; right: 40px; top: 175px; height: 300px;
    border-radius: 22px 22px 4px 4px;
    background: linear-gradient(165deg, var(--train-steel) 0%, var(--train-blue) 38%, var(--train-shadow) 100%);
    border: 2px solid rgba(170,190,205,0.45);
    box-shadow: 0 0 40px rgba(0,0,0,0.6);
  }
  .front-cover__wreck {
    position: absolute; left: 0; right: 0; bottom: 0; height: 210px;
    background: linear-gradient(0deg, var(--flame-deep) 0%, var(--flame-bright) 30%, var(--flame-glow) 40%, rgba(130,120,110,0.85) 62%, rgba(0,0,0,0) 100%);
  }
  .title {
    position: absolute; top: 18px; left: 30px; right: 30px;
    font-family: "Anton", sans-serif; text-transform: uppercase;
    color: var(--paper-white); line-height: 0.98; letter-spacing: 4px;
    text-align: center;
  }
  .title__line { display: block; font-size: 84px; }
  .title__line--accent { text-shadow: 5px 4px 0 var(--accent-red); }
  .author-block {
    position: absolute; left: 0; right: 0; top: 400px; text-align: center;
  }
  .author-block__label {
    color: var(--paper-white); font-size: 25px; letter-spacing: 4px;
    text-transform: uppercase;
  }
  .author-block__name {
    display: inline-block; margin-top: 2px; padding: 2px 18px;
    background: var(--band-red); color: var(--paper-white);
    font-size: 31px; font-weight: 600; letter-spacing: 4px;
    text-transform: uppercase;
  }
</style>
</head>
<body>
  <main class="spread">
    <section class="back-cover">
      <h2 class="back-cover__heading">The brilliant<br>fictional<br>story of strangers<br>who meet on a train</h2>
      <div class="back-cover__blurb">
        <p>After the train crashes and bursts into flames, they take the luggage of different passengers and decide to make a new life together.</p>
        <p>Culminating in a murder which they believe they can get away with forever. The book is a thriller and engages the reader in suspense, excitement and anxiety.</p>
      </div>
      <div class="back-cover__flames" role="img" aria-label="Photograph of roaring flames"></div>
    </section>

    <section class="spine">
      <span class="spine__text">Quiet Ledgers</span>
      <span class="spine__rule"></span>
      <span class="spine__text spine__author">Brent Hollis</span>
    </section>

    <section class="front-cover">
      <div class="front-cover__smoke" role="img" aria-label="Dark smoke drifting over the scene"></div>
      <div class="front-cover__train" role="img" aria-label="Photograph of a battered blue metro train with shattered windows, seen from the front"></div>
      <div class="front-cover__wreck" role="img" aria-label="Photograph of crash wreckage engulfed in flames"></div>
      <h1 class="title">
        <span class="title__line">Quiet</span>
        <span class="title__line title__line--accent">Ledgers</span>
      </h1>
      <div class="author-block">
        <p class="author-block__label">Debut Author</p>
        <p class="author-block__name">Brent Hollis</p>
      </div>
    </section>
  </main>
</body>
</html>
```